brindle's business card for earthmoving and tipper hire business.

I have a small earthmoving and tipper truck company. I am aiming for the smaller jobs that the big guys don't want. I am also Doing grass slashing and fire hazard reduction work. I would like to see some earthy colors, greens browns etc. I have a tractor with a front end loader attachment, and a 22 ton tipper. I would like to maybe have a silhouette of a tipper and tractor/slasher/loader setup in centre with my business name over the top and details to one side or something like that

Industry/Entity Type

Business

Contact Information for Business Card

Brindle's small earthworks and tipper hireToowoombaABN: 47781050480PH 0479126773Email brindle.4@fenwickmail.com

Font styles to use
Sans Serif

Colors
fbee3d
abd036
85cae6
f78f20

Requirements
Nice to have
• Earthy colors . business name in blue

```html
<!DOCTYPE html>
<html lang="en">
<head>
<meta charset="utf-8">
<title>Brindle's Earthworks and Tipper Hire</title>
<link rel="stylesheet" href="https://fonts.googleapis.com/css2?family=Lato:wght@700&family=Marcellus&display=swap">
<style>
  :root {
    --brown-deep: #472a22;
    --brown-top: #4a2d25;
    --brown-mid: #5a3a2f;
    --field-green: #4a8158;
    --sky-blue: #b8dcea;
    --chalk: #f4f1ec;
  }
  html, body {
    margin: 0;
    padding: 0;
    width: 1200px;
    height: 741px;
    overflow: hidden;
    background: var(--brown-deep);
  }
  .card {
    position: relative;
    width: 1200px;
    height: 741px;
    overflow: hidden;
  }
  .card__art {
    position: absolute;
    inset: 0;
    display: block;
  }
  .brand-name {
    font-family: "Lato", "Helvetica Neue", Arial, sans-serif;
    font-weight: 700;
    font-size: 170px;
    fill: var(--sky-blue);
  }
  .tagline {
    font-family: "Marcellus", "Optima", Georgia, serif;
    font-size: 27px;
    fill: var(--chalk);
  }
</style>
</head>
<body>
<main class="card">
  <svg class="card__art" width="1200" height="741" viewBox="0 0 1200 741" xmlns="http://www.w3.org/2000/svg">
    <defs>
      <linearGradient id="groundShade" x1="0" y1="0" x2="0" y2="1">
        <stop offset="0" stop-color="var(--brown-mid)"/>
        <stop offset="1" stop-color="var(--brown-deep)"/>
      </linearGradient>
      <radialGradient id="truckTone" cx="0.5" cy="0.5" r="0.5">
        <stop offset="0" stop-color="#4e3a2c" stop-opacity="0.95"/>
        <stop offset="0.7" stop-color="#4e3a2c" stop-opacity="0.6"/>
        <stop offset="1" stop-color="#4e3a2c" stop-opacity="0"/>
      </radialGradient>
    </defs>

    <rect class="field-band" width="1200" height="741" fill="var(--field-green)"/>
    <path class="sky-curve" d="M189 0 C330 110 520 165 700 162 C900 158 1080 115 1200 67 L1200 0 Z" fill="var(--brown-top)"/>
    <path class="ground-curve" d="M0 251 C250 320 500 340 700 360 C900 380 1080 420 1200 463 L1200 741 L0 741 Z" fill="url(#groundShade)"/>

    <g role="img" aria-label="Tipper truck silhouette in dark brown">
      <ellipse cx="200" cy="180" rx="140" ry="110" fill="url(#truckTone)"/>
    </g>

    <text class="brand-name" x="405" y="568" textLength="703" lengthAdjust="spacingAndGlyphs">Brindle's</text>

    <text class="tagline" x="406" y="609" textLength="698" lengthAdjust="spacing">EARTHWORKS AND TIPPER HIRE</text>
  </svg>
</main>
</body>
</html>
```